Online Prescription Eyeglass Lens Company Needs a Website

*Update new name to ClearPair. Thx

We are eye doctors with a lab that need a website for a new company based in Southern California called ClearPair. We replace old prescription lenses with new ones next day for most lenses. Patients select the lenses and give us the prescription. We then send a box with a prepaid shipping label. Place the frames in the box and drop them in the mail to our lab. We will custom make new lenses, fit them back into your frames and send them back to you. We would like to compete with www.vizora.com and offer affordable lenses for single vision, bifocal, progressive, sunglass lenses at an affordable price with next day shipping.
Updates

Hi Designers, We have a new name called ClearPair. Can we have the website design reflect the new name and we'll pick our favorites. Thx

Update: The new name is OptiNova . I have not made very many changes or feedback to the submissions because we were bidding for a .com. We won and our new name is OptiNova . This is the last name change.. Please have the website reflect the new name and I'll be providing feedback on the websites . ( I have a separate project for the logo people are working on, so don't worry about creating a logo). Look forward to the submissions. Thanks everyone.

Hi, Just leave the name as ClearPair for now. I will narrow down top designs tonight. Thx

Target Market(s)

Anyone that wears prescription or nonprescription glasses or sunglasses that want next day shipping.

Industry/Entity Type

Eyewear

Number of Pages Required

4 page

Font styles to use
Serif

Colors

Designer to choose colors to be used in the design.

Requirements
Must have
• I need a website that can compete with https://www.vizora.com/.
• We are different from vizora because we can offer same day service or next day shipping.
• It needs to have website that offers the lenses available listed below.
• Needs to be able to upload a prescription and payment feature.
• Pictures of different types of options with small info about each lens option.
• Template Pricing (just use numbers from $79-$179 for now)
• SINGLE VISION LENSES
• HIGH INDEX LENSES
• READING LENSES
• DIGITAL HD PROGRESSIVE LENSES
• RX & NON-RX SUNGLASSES
• RX & NON-RX POLARIZED SUNGLASSES
• COMPUTER LENSES
• TRANSITION LENSES
• BI-FOCAL LENSES

```html
<!DOCTYPE html>
<html lang="en">
<head>
<meta charset="utf-8">
<title>ClearPair — Prescription Lenses</title>
<link rel="stylesheet" href="https://fonts.googleapis.com/css2?family=Jost:wght@400;500;600&family=Libre+Baskerville&display=swap">
<style>
:root{
  --blue:#6bb6e3;
  --blue-deep:#4fa3d8;
  --ink:#262d3b;
  --body:#3b3f47;
  --white:#ffffff;
  --grey-band:#efefef;
  --lens-band:#f6f7f9;
  --hero-dark:#4a4441;
  --footer-dark:#2b2a2a;
  --line:#d7dde3;
}
*{box-sizing:border-box;margin:0;padding:0}
html,body{width:1200px;height:2230px;overflow:hidden;background:var(--white)}
body{font-family:"Jost",Arial,sans-serif;color:var(--body);position:relative}
.abs{position:absolute}

/* header */
.site-header{position:absolute;left:0;top:0;width:1200px;height:94px;background:var(--white)}
.brand{position:absolute;left:141px;top:30px;font-family:"Jost",sans-serif;font-weight:500;font-size:31px;color:var(--blue);letter-spacing:.3px}
.main-nav a{position:absolute;top:39px;font-size:12px;font-weight:500;color:var(--ink);text-decoration:none;letter-spacing:.3px;text-transform:uppercase}
.main-nav a.active{color:var(--blue)}
.phone-pill{position:absolute;left:904px;top:30px;width:155px;height:35px;border-radius:18px;background:var(--blue);color:var(--white);font-size:15px;line-height:35px;padding-left:46px}
.phone-pill .dot{position:absolute;left:2px;top:2px;width:31px;height:31px;border-radius:50%;background:#8ac6ea;display:flex;align-items:center;justify-content:center}

/* hero */
.hero{position:absolute;left:0;top:94px;width:1200px;height:444px;background:linear-gradient(90deg,#4b4643 0%,#4a4542 45%,#5e3a33 62%,#8a3a36 78%,#4c3a37 100%)}
.hero-photo{position:absolute;left:540px;top:0;width:660px;height:444px;background:radial-gradient(ellipse at 40% 40%,#c79a85 0%,#a85a4a 35%,#7a2a2a 65%,rgba(74,69,66,0) 100%)}
.hero-title{position:absolute;left:143px;top:140px;width:440px;font-family:"Libre Baskerville",Georgia,serif;color:var(--white);font-size:20px;line-height:29px}
.btn{position:absolute;display:block;border:2px solid var(--blue);font-size:12px;font-weight:600;letter-spacing:.6px;text-transform:uppercase;text-align:center;text-decoration:none}
.btn-hero{left:143px;top:355px;width:107px;height:33px;line-height:29px;color:var(--white);background:transparent}
.slider-dots{position:absolute;left:143px;top:347px;display:flex;gap:5px;align-items:center}
.slider-dots span{width:7px;height:7px;border-radius:50%;background:var(--blue)}
.slider-dots span.on{width:14px;border-radius:4px;background:var(--white)}

/* about */
.section-title{position:absolute;left:0;width:1200px;text-align:center;font-family:"Jost",sans-serif;font-weight:500;font-size:29px;color:var(--ink)}
.section-title em{font-style:normal;color:var(--blue)}
.about-text{position:absolute;left:146px;top:660px;width:908px;text-align:center;font-size:13px;line-height:22px;color:var(--body)}
.btn-dark{color:var(--ink);background:var(--white)}

/* products */
.products{position:absolute;left:0;top:858px;width:1200px;height:764px;background:var(--grey-band)}
.title-rule{position:absolute;left:583px;width:34px;height:1px;background:#c9cdd2}
.product-card{position:absolute;width:204px;height:184px;background:var(--white);text-align:center}
.product-photo{position:absolute;left:57px;top:-45px;width:90px;height:90px;border-radius:50%;border:4px solid #f2f2f2}
.product-name{position:absolute;left:0;top:62px;width:204px;font-size:15px;line-height:19px;font-weight:500;color:var(--blue)}
.product-copy{position:absolute;left:14px;top:108px;width:176px;font-size:10.5px;line-height:14px;color:var(--body)}
.product-more{position:absolute;left:83px;bottom:0}
.btn-view{left:550px;top:1530px;width:98px;height:31px;line-height:27px;color:var(--ink);background:var(--white)}

/* lenses band */
.our-lenses{position:absolute;left:0;top:1622px;width:1200px;height:330px;background:var(--lens-band)}
.lenses-photo{position:absolute;left:773px;top:0;width:427px;height:330px;background:radial-gradient(ellipse at 38% 45%,#e2c2ad 0%,#d9b29a 30%,#bfd9e2 60%,rgba(246,247,249,0) 82%)}
.lenses-title{position:absolute;left:143px;top:74px;font-size:29px;font-weight:500;color:var(--blue)}
.lenses-text{position:absolute;left:143px;top:122px;width:580px;font-size:13px;line-height:22px;color:var(--ink)}
.lenses-price{position:absolute;left:143px;top:175px;font-size:16px;color:var(--ink)}
.btn-lenses{left:141px;top:220px;width:198px;height:31px;line-height:27px;color:var(--ink);background:var(--white)}

/* footer */
.site-footer{position:absolute;left:0;top:1952px;width:1200px;height:234px;background:linear-gradient(180deg,#2f2e2e 0%,#3a3836 55%,#262525 100%);color:var(--white)}
.footer-col{position:absolute;top:36px}
.footer-col h4{font-size:14px;font-weight:500;color:var(--white)}
.footer-col h4::after{content:"";display:block;width:40px;height:1px;background:var(--white);margin-top:12px}
.footer-divider{position:absolute;top:30px;height:190px;border-left:1px dashed rgba(255,255,255,.35)}
.quick-links{list-style:none;margin-top:18px}
.quick-links li{font-size:11.5px;line-height:21.5px;color:#e8e8e8}
.quick-links li::before{content:"»";margin-right:12px}
.contact-list{list-style:none;margin-top:16px}
.contact-list li{display:flex;gap:8px;font-size:11px;line-height:15px;color:#e8e8e8;margin-bottom:12px;width:150px}
.contact-list svg{flex:0 0 14px;margin-top:1px}
.location-map{width:208px;height:107px;margin-top:20px;background:linear-gradient(135deg,#e9ecef,#d9e2e8);border:2px solid #cfd4d8}
.social-row{display:flex;gap:7px;margin-top:24px}
.social-row span{width:24px;height:24px;border-radius:50%;background:var(--blue)}
.footer-brand{margin-top:24px;font-size:28px;font-weight:500;color:var(--blue)}
.copyright{position:absolute;left:0;top:2186px;width:1200px;height:44px;background:#7cc0e6;color:var(--white);text-align:center;font-size:11px;line-height:44px}
</style>
</head>
<body>

<header class="site-header">
  <div class="brand">ClearPair</div>
  <nav class="main-nav">
    <a class="active" href="#" style="left:478px">Home</a>
    <a href="#" style="left:543px">About Us</a>
    <a href="#" style="left:634px">Products</a>
    <a href="#" style="left:730px">FAQ's</a>
    <a href="#" style="left:795px">Contact Us</a>
  </nav>
  <div class="phone-pill">
    <span class="dot"><svg width="14" height="14" viewBox="0 0 24 24"><path fill="#fff" d="M6.6 10.8a15 15 0 0 0 6.6 6.6l2.2-2.2a1 1 0 0 1 1-.25 11.4 11.4 0 0 0 3.6.57 1 1 0 0 1 1 1V20a1 1 0 0 1-1 1A17 17 0 0 1 3 4a1 1 0 0 1 1-1h3.5a1 1 0 0 1 1 1c0 1.25.2 2.45.57 3.57a1 1 0 0 1-.25 1z"/></svg></span>
    (555)-010-4200
  </div>
</header>

<section class="hero">
  <div class="hero-photo" role="img" aria-label="Photo of a couple wearing dark-framed prescription glasses"></div>
  <h1 class="hero-title">We Are Eye Doctors With A Laboratory &amp; We Are New Business Based In Southern California, USA</h1>
  <a class="btn btn-hero" href="#">Shop Now</a>
  <div class="slider-dots"><span class="on"></span><span></span><span></span></div>
</section>

<section class="about">
  <h2 class="section-title" style="top:587px">About <em>ClearPair</em></h2>
  <p class="about-text">Lorem ipsum dolor sit amet, consectetuer adipiscing elit, sed diam nonummy nibh euismod tincidunt ut laoreet dolore magna aliquam erat volutpat. Ut wisi enim ad minim veniam, quis nostrud exerci tation ullamcorper suscipit lobortis nisl ut aliquip ex ea commodo consequat. Duis autem vel eum iriure dolor in hendrerit in vulputate velit esse molestie consequat, vel illum dolore eu feugiat nulla facilisis at vero eros et accumsan et iusto odio dignissim qui blandit praesent luptatum zzril delenit augue duis dolore te feugait nulla facilisi sed diam nonummy nibh euismod tincidunt ut laoreet dolore magna aliquam erat.</p>
  <a class="btn btn-dark" href="#" style="left:550px;top:763px;width:98px;height:31px;line-height:27px">Read More</a>
</section>

<section class="products">
  <h2 class="section-title" style="top:55px">Popular <em>Products</em></h2>
  <div class="title-rule" style="top:106px"></div>

  <article class="product-card" style="left:141px;top:186px">
    <div class="product-photo" role="img" aria-label="Window view seen through a single vision lens" style="background:radial-gradient(circle,#cfe3ef,#8aa9bb)"></div>
    <h3 class="product-name">Single Vision<br>Lenses</h3>
    <p class="product-copy">Lorem ipsum dolor sit amet constuer adipiscing elit, sed diam nonummy nibh euismod tincidunt ut.</p>
    <svg class="product-more" width="38" height="14" viewBox="0 0 38 14"><path d="M0 14 L19 0 L38 14Z" fill="var(--blue)"/><path d="M19 5v8M15 9h8" stroke="#fff" stroke-width="2"/></svg>
  </article>
  <article class="product-card" style="left:379px;top:186px">
    <div class="product-photo" role="img" aria-label="Close-up of an eye behind a high index lens" style="background:radial-gradient(circle,#c98a6a,#6b3a28)"></div>
    <h3 class="product-name">High Index<br>Lenses</h3>
    <p class="product-copy">Lorem ipsum dolor sit amet constuer adipiscing elit, sed diam nonummy nibh euismod tincidunt ut.</p>
    <svg class="product-more" width="38" height="14" viewBox="0 0 38 14"><path d="M0 14 L19 0 L38 14Z" fill="var(--blue)"/><path d="M19 5v8M15 9h8" stroke="#fff" stroke-width="2"/></svg>
  </article>
  <article class="product-card" style="left:617px;top:186px">
    <div class="product-photo" role="img" aria-label="Reading glasses resting on a printed page" style="background:radial-gradient(circle,#f1ece4,#9b7a5c)"></div>
    <h3 class="product-name">Reading<br>Lenses</h3>
    <p class="product-copy">Lorem ipsum dolor sit amet constuer adipiscing elit, sed diam nonummy nibh euismod tincidunt ut.</p>
    <svg class="product-more" width="38" height="14" viewBox="0 0 38 14"><path d="M0 14 L19 0 L38 14Z" fill="var(--blue)"/><path d="M19 5v8M15 9h8" stroke="#fff" stroke-width="2"/></svg>
  </article>
  <article class="product-card" style="left:855px;top:186px">
    <div class="product-photo" role="img" aria-label="Room seen through a progressive lens" style="background:radial-gradient(circle,#eef3f6,#a9bdc8)"></div>
    <h3 class="product-name">Digital Hd<br>Progressive Lenses</h3>
    <p class="product-copy">Lorem ipsum dolor sit amet constuer adipiscing elit, sed diam nonummy nibh euismod tincidunt ut.</p>
    <svg class="product-more" width="38" height="14" viewBox="0 0 38 14"><path d="M0 14 L19 0 L38 14Z" fill="var(--blue)"/><path d="M19 5v8M15 9h8" stroke="#fff" stroke-width="2"/></svg>
  </article>

  <article class="product-card" style="left:141px;top:453px">
    <div class="product-photo" role="img" aria-label="Portrait of a woman wearing sunglasses" style="background:radial-gradient(circle,#e3b79b,#8a5a42)"></div>
    <h3 class="product-name">Rx &amp; Non-Rx<br>Sunglasses</h3>
    <p class="product-copy">Lorem ipsum dolor sit amet constuer adipiscing elit, sed diam nonummy nibh euismod tincidunt ut.</p>
    <svg class="product-more" width="38" height="14" viewBox="0 0 38 14"><path d="M0 14 L19 0 L38 14Z" fill="var(--blue)"/><path d="M19 5v8M15 9h8" stroke="#fff" stroke-width="2"/></svg>
  </article>
  <article class="product-card" style="left:379px;top:453px">
    <div class="product-photo" role="img" aria-label="Black polarized glasses on white" style="background:radial-gradient(circle,#ffffff,#cfcfcf)"></div>
    <h3 class="product-name">Rx &amp; Non-Rx<br>Polarized Sunglasses</h3>
    <p class="product-copy">Lorem ipsum dolor sit amet constuer adipiscing elit, sed diam nonummy nibh euismod tincidunt ut.</p>
    <svg class="product-more" width="38" height="14" viewBox="0 0 38 14"><path d="M0 14 L19 0 L38 14Z" fill="var(--blue)"/><path d="M19 5v8M15 9h8" stroke="#fff" stroke-width="2"/></svg>
  </article>
  <article class="product-card" style="left:617px;top:453px">
    <div class="product-photo" role="img" aria-label="Computer screen reflected in a lens" style="background:radial-gradient(circle,#8fe0c8,#2f6e5e)"></div>
    <h3 class="product-name">Computer<br>Lenses</h3>
    <p class="product-copy">Lorem ipsum dolor sit amet constuer adipiscing elit, sed diam nonummy nibh euismod tincidunt ut.</p>
    <svg class="product-more" width="38" height="14" viewBox="0 0 38 14"><path d="M0 14 L19 0 L38 14Z" fill="var(--blue)"/><path d="M19 5v8M15 9h8" stroke="#fff" stroke-width="2"/></svg>
  </article>
  <article class="product-card" style="left:855px;top:453px">
    <div class="product-photo" role="img" aria-label="Portrait of a man wearing transition lenses" style="background:radial-gradient(circle,#d9b39a,#6d5446)"></div>
    <h3 class="product-name">Transition<br>Lenses</h3>
    <p class="product-copy">Lorem ipsum dolor sit amet constuer adipiscing elit, sed diam nonummy nibh euismod tincidunt ut.</p>
    <svg class="product-more" width="38" height="14" viewBox="0 0 38 14"><path d="M0 14 L19 0 L38 14Z" fill="var(--blue)"/><path d="M19 5v8M15 9h8" stroke="#fff" stroke-width="2"/></svg>
  </article>
</section>
<a class="btn btn-view" href="#">View All</a>

<section class="our-lenses">
  <div class="lenses-photo" role="img" aria-label="Woman adjusting her glasses in front of an eye chart"></div>
  <h2 class="lenses-title">Our Lenses</h2>
  <p class="lenses-text">Lorem ipsum dolor sit amet, consectetuer adipiscing elit, sed diam nonummy nibh euismod tincidunt ut laoreet dolore magna aliquam erat volutpat Ut wisi enim ad minim veniam.</p>
  <p class="lenses-price">Our lenses Prices starts from &nbsp;$79-$179</p>
  <a class="btn btn-lenses" href="#">Learn About Our Lenses</a>
</section>

<footer class="site-footer">
  <div class="footer-col" style="left:140px">
    <h4>Quick Links</h4>
    <ul class="quick-links">
      <li>Home</li><li>About Us</li><li>Products</li><li>FAQ's</li><li>Contact Us</li>
    </ul>
  </div>
  <div class="footer-divider" style="left:280px"></div>
  <div class="footer-col" style="left:335px">
    <h4>Contact Details</h4>
    <ul class="contact-list">
      <li><svg width="14" height="14" viewBox="0 0 24 24"><path fill="#fff" d="M12 2a7 7 0 0 0-7 7c0 5 7 13 7 13s7-8 7-13a7 7 0 0 0-7-7zm0 9.5A2.5 2.5 0 1 1 12 6.5a2.5 2.5 0 0 1 0 5z"/></svg><span>123 Lorem ipsum dolor sit amet constuer adipiscing.</span></li>
      <li><svg width="14" height="14" viewBox="0 0 24 24"><path fill="#fff" d="M6.6 10.8a15 15 0 0 0 6.6 6.6l2.2-2.2a1 1 0 0 1 1-.25 11.4 11.4 0 0 0 3.6.57 1 1 0 0 1 1 1V20a1 1 0 0 1-1 1A17 17 0 0 1 3 4a1 1 0 0 1 1-1h3.5a1 1 0 0 1 1 1c0 1.25.2 2.45.57 3.57a1 1 0 0 1-.25 1z"/></svg><span>(555)-010-4200</span></li>
      <li><svg width="14" height="14" viewBox="0 0 24 24"><path fill="#fff" d="M6 2h12v6H6zM3 9h18v9h-3v4H6v-4H3zm5 6v5h8v-5z"/></svg><span>(555)-010-4200</span></li>
      <li><svg width="14" height="14" viewBox="0 0 24 24"><path fill="#fff" d="M2 5h20v14H2zm2 2v.5l8 5 8-5V7l-8 5z"/></svg><span>hello@clearpair-mail.com</span></li>
    </ul>
  </div>
  <div class="footer-divider" style="left:538px"></div>
  <div class="footer-col" style="left:595px">
    <h4>Location Map</h4>
    <div class="location-map" role="img" aria-label="Road map showing the store location"></div>
  </div>
  <div class="footer-divider" style="left:860px"></div>
  <div class="footer-col" style="left:914px">
    <h4>Follow Us</h4>
    <div class="social-row"><span></span><span></span><span></span><span></span><span></span></div>
    <div class="footer-brand">ClearPair</div>
  </div>
</footer>
<div class="copyright">Copyright © 2017 ClearPair. All Rights Reserved.</div>

</body>
</html>
```